Business card design for IT consulting company

Looking for a simple, modern, clean business card design.
Open to reworking our existing logo.

Attached is our current business cards which we do not like.
Ideally double sided with something simple on the back.
Rectangle / Horizonal only.
No rounded edges on the card.
White as the dominate color is preferred.

Target Market(s)

clients, legal, oil & gas, medical, professionals

Industry/Entity Type

IT, tech, consulting

Contact Information for Business Card

Name, Title, email, phone, cell, website

Font styles to use
Sans Serif

Requirements
Must have
• Clean design
Should not have
• loud colors or unusual fonts, etc

```html
<!DOCTYPE html>
<html lang="en">
<head>
<meta charset="utf-8">
<title>KV3 Solutions — Business Card</title>
<link rel="stylesheet" href="https://fonts.googleapis.com/css2?family=Jost:wght@400;500;600;700&display=swap">
<style>
  :root {
    --page: #ffffff;
    --ink: #000000;
    --paper: #ffffff;
    --card-shadow: rgba(0, 0, 0, 0.28);
  }
  * { margin: 0; padding: 0; box-sizing: border-box; }
  html, body {
    width: 1200px;
    height: 675px;
    overflow: hidden;
    background: var(--page);
    font-family: "Jost", "Futura", sans-serif;
    color: var(--ink);
  }
  .canvas {
    position: relative;
    width: 1200px;
    height: 675px;
  }
  .card {
    position: absolute;
    top: 234px;
    width: 370px;
    height: 211px;
  }

  /* Back side */
  .card-back {
    left: 206px;
    background: var(--ink);
    display: flex;
    align-items: center;
    justify-content: center;
  }
  .brand-name {
    color: var(--paper);
    font-size: 29px;
    font-weight: 500;
    letter-spacing: 0.01em;
    margin-top: -2px;
  }

  /* Front side */
  .card-front {
    left: 632px;
    background: var(--paper);
    box-shadow: 4px 6px 10px var(--card-shadow);
  }
  .person-name {
    position: absolute;
    left: 28px;
    top: 24px;
    font-size: 17px;
    font-weight: 700;
    letter-spacing: 0.09em;
    line-height: 1;
  }
  .person-title {
    position: absolute;
    left: 28px;
    top: 46px;
    font-size: 11px;
    font-weight: 400;
    letter-spacing: 0.28em;
    line-height: 1;
  }
  .contact-box {
    position: absolute;
    left: 29px;
    top: 78px;
    width: 135px;
    height: 104px;
    border: 1.4px solid var(--ink);
    border-radius: 7px;
    padding: 8px 0 0 11px;
    list-style: none;
  }
  .contact-item {
    display: flex;
    align-items: center;
    height: 23.5px;
    font-size: 10.5px;
    font-weight: 400;
    letter-spacing: 0.02em;
  }
  .contact-icon {
    width: 12px;
    height: 12px;
    margin-right: 10px;
    flex: none;
    fill: var(--ink);
  }
  .brand-mark-text {
    position: absolute;
    left: 244px;
    top: 30px;
    width: 104px;
    height: 86px;
    display: flex;
    align-items: center;
    justify-content: center;
    font-size: 50px;
    font-weight: 600;
    letter-spacing: 0.04em;
    line-height: 1;
  }
  .corner-square {
    position: absolute;
    left: 336px;
    top: 176px;
    width: 5px;
    height: 5px;
    background: var(--ink);
  }
</style>
</head>
<body>
<main class="canvas">

  <section class="card card-back" aria-label="Card back">
    <span class="brand-name">KV3 Solutions</span>
  </section>

  <section class="card card-front" aria-label="Card front">
    <h1 class="person-name">Daniel RHEE</h1>
    <p class="person-title">IT consultant</p>

    <ul class="contact-box">
      <li class="contact-item">
        <svg class="contact-icon" viewBox="0 0 24 24" aria-hidden="true">
          <path d="M2 5h20v14H2z M2 5l10 8 10-8" fill="var(--ink)"/>
          <path d="M3 6.2l9 7 9-7" fill="none" stroke="#fff" stroke-width="1.6"/>
        </svg>
        <span>daniel.rhee@kv3.ca</span>
      </li>
      <li class="contact-item">
        <svg class="contact-icon" viewBox="0 0 24 24" aria-hidden="true">
          <path d="M6.6 10.8c1.4 2.8 3.8 5.1 6.6 6.6l2.2-2.2c.3-.3.7-.4 1-.2 1.1.4 2.3.6 3.6.6.6 0 1 .4 1 1V20c0 .6-.4 1-1 1C10.6 21 3 13.4 3 4c0-.6.4-1 1-1h3.5c.6 0 1 .4 1 1 0 1.3.2 2.5.6 3.6.1.3 0 .7-.2 1z"/>
        </svg>
        <span>(888) 555-0142</span>
      </li>
      <li class="contact-item">
        <svg class="contact-icon" viewBox="0 0 24 24" aria-hidden="true">
          <rect x="7" y="1.5" width="10" height="21" rx="2"/>
          <rect x="8.6" y="4" width="6.8" height="14" fill="#fff"/>
          <circle cx="12" cy="20.2" r="1" fill="#fff"/>
        </svg>
        <span>(604) 555-0187</span>
      </li>
      <li class="contact-item">
        <svg class="contact-icon" viewBox="0 0 24 24" aria-hidden="true">
          <path d="M22 2L2 10.5l7.5 3 3 8.5z"/>
        </svg>
        <span>www.kv3.ca</span>
      </li>
    </ul>

    <div class="brand-mark-text">KV3</div>
    <div class="corner-square" aria-hidden="true"></div>
  </section>

</main>
</body>
</html>
```